Promotion for Mobile Tyre Fitting on our site

We need a promotion banner to advertise mobile tyre fitting.
We sell tyres. Now we also sell a service where a mobile tyre fitter will come to the customers workplace or home and fit the tyres. This service is currently available in Brisbane and Melbourne
Benfits to the customer
It is fast and convenient.
No travel time
No wait time
Fast - usually complete within 30 minutes.
Save money by buying online
Save time
The banner should be designed so we can add more locations as they become available.
A graphic showing tyres being fitted on a car at a suburban house, or in an office car park may be appropriate. Or some kind of stylised graphic indicating the message that we come to you.
www.lowtreadhub.com.au is our site. Please look at the existing banners to ensure you create banners of the correct size. You can see a large banner beside the video and smaller banner under the Wheel Picker. We want both sizes.
Updates
Project Deadline Extended
Reason: Something has come up so I don't have time today to check progress and provide feedback so I am extending by 1 day.
I want to be fair and not leave feedback till the last minute.
I hope this doesn't cause any inconvenience.
thanks
Kev

```html
<!DOCTYPE html>
<html lang="en">
<head>
<meta charset="utf-8">
<title>Mobile Tyre Fitting – Promotion Banners</title>
<link rel="stylesheet" href="https://fonts.googleapis.com/css2?family=Arimo:wght@400;700&family=Archivo+Narrow:wght@400;500&display=swap">
<style>
  :root {
    --page: #ffffff;
    --navy: #0d3f8f;
    --navy-deep: #0a2f6b;
    --red: #b3121b;
    --frame: #2a2a2a;
    --sky-light: #8fbfdc;
    --sky-mid: #5b98c3;
    --sky-deep: #2f6e9f;
    --white: #ffffff;
    --photo-light: #e9ecef;
    --photo-mid: #b9bec4;
    --photo-dark: #6d737a;
  }
  html, body {
    margin: 0;
    padding: 0;
    width: 1080px;
    height: 1200px;
    overflow: hidden;
    background: var(--page);
  }
  .canvas {
    position: relative;
    width: 1080px;
    height: 1200px;
    font-family: "Arimo", Arial, sans-serif;
  }

  /* Large banner */
  .banner-large {
    position: absolute;
    left: 19px;
    top: 19px;
    width: 1044px;
    height: 766px;
    box-sizing: border-box;
    border: 2px solid var(--frame);
    background: var(--white);
    overflow: hidden;
  }
  .banner-large .headline-main {
    position: absolute;
    left: 56px;
    top: 40px;
    margin: 0;
    font-weight: 700;
    font-size: 158px;
    line-height: 1;
    letter-spacing: -3px;
    color: var(--navy);
  }
  .banner-large .headline-sub {
    position: absolute;
    left: 58px;
    top: 190px;
    margin: 0;
    font-family: "Archivo Narrow", "Arial Narrow", sans-serif;
    font-weight: 400;
    font-size: 92px;
    line-height: 1;
    color: var(--navy);
  }
  .banner-large .benefits {
    position: absolute;
    left: 140px;
    top: 320px;
    margin: 0;
    padding: 0;
    list-style: none;
    font-size: 52px;
    line-height: 72px;
    color: var(--red);
  }
  .benefits li::before {
    content: "•";
    display: inline-block;
    width: 34px;
  }
  .banner-large .locations {
    position: absolute;
    left: 40px;
    top: 596px;
    margin: 0;
    font-size: 46px;
    line-height: 1;
    color: var(--navy);
  }
  .banner-large .site-address {
    position: absolute;
    left: 40px;
    top: 664px;
    margin: 0;
    font-weight: 700;
    font-size: 48px;
    line-height: 1;
    color: var(--red);
  }
  .banner-large .fitting-photo {
    position: absolute;
    left: 555px;
    top: 178px;
    width: 460px;
    height: 460px;
  }

  /* Small banner */
  .banner-small {
    position: absolute;
    left: 125px;
    top: 845px;
    width: 835px;
    height: 288px;
    box-sizing: border-box;
    border: 2px solid var(--navy-deep);
    background: linear-gradient(100deg, var(--sky-light) 0%, var(--sky-mid) 45%, var(--sky-deep) 100%);
    overflow: hidden;
    color: var(--white);
  }
  .banner-small .fitting-photo {
    position: absolute;
    left: 560px;
    top: -10px;
    width: 300px;
    height: 300px;
  }
  .banner-small .locations {
    position: absolute;
    left: 30px;
    top: 26px;
    margin: 0;
    font-size: 36px;
    line-height: 1;
  }
  .banner-small .headline-main {
    position: absolute;
    left: 18px;
    top: 80px;
    margin: 0;
    font-weight: 700;
    font-size: 80px;
    line-height: 1;
    letter-spacing: -1px;
  }
  .banner-small .headline-sub {
    position: absolute;
    left: 20px;
    top: 160px;
    margin: 0;
    font-family: "Archivo Narrow", "Arial Narrow", sans-serif;
    font-weight: 500;
    font-size: 54px;
    line-height: 1;
  }
  .banner-small .benefits {
    position: absolute;
    left: 338px;
    top: 94px;
    margin: 0;
    padding: 0;
    list-style: none;
    font-size: 28px;
    line-height: 36px;
  }
  .banner-small .benefits li::before {
    width: 20px;
  }
  .banner-small .site-address {
    position: absolute;
    left: 26px;
    top: 232px;
    margin: 0;
    font-weight: 700;
    font-size: 36px;
    line-height: 1;
  }
</style>
</head>
<body>
<main class="canvas">

  <section class="banner-large" aria-label="Large promotion banner">
    <h1 class="headline-main">MOBILE</h1>
    <p class="headline-sub">TYRE FITTING</p>
    <ul class="benefits">
      <li>EASIER</li>
      <li>FASTER</li>
      <li>CHEAPER</li>
    </ul>
    <svg class="fitting-photo" viewBox="0 0 460 460" role="img" aria-label="Photo of hands tightening wheel nuts on a car tyre with a cross wrench">
      <defs>
        <radialGradient id="photo-tone-large" cx="45%" cy="40%" r="60%">
          <stop offset="0%" stop-color="var(--photo-light)"/>
          <stop offset="60%" stop-color="var(--photo-mid)"/>
          <stop offset="100%" stop-color="var(--photo-dark)"/>
        </radialGradient>
        <radialGradient id="photo-halo" cx="50%" cy="50%" r="50%">
          <stop offset="88%" stop-color="#000" stop-opacity="0.25"/>
          <stop offset="100%" stop-color="#000" stop-opacity="0"/>
        </radialGradient>
      </defs>
      <circle cx="230" cy="230" r="230" fill="url(#photo-halo)"/>
      <circle cx="230" cy="230" r="211" fill="url(#photo-tone-large)"/>
    </svg>
    <p class="locations">BRISBANE &amp; MELBOURNE</p>
    <p class="site-address">www.lowtreadhub.com.au</p>
  </section>

  <section class="banner-small" aria-label="Small promotion banner">
    <svg class="fitting-photo" viewBox="0 0 300 300" role="img" aria-label="Photo of hands tightening wheel nuts on a car tyre with a cross wrench">
      <defs>
        <radialGradient id="photo-tone-small" cx="40%" cy="45%" r="60%">
          <stop offset="0%" stop-color="var(--photo-light)"/>
          <stop offset="65%" stop-color="var(--photo-mid)"/>
          <stop offset="100%" stop-color="var(--photo-dark)"/>
        </radialGradient>
      </defs>
      <circle cx="180" cy="150" r="150" fill="url(#photo-tone-small)"/>
    </svg>
    <p class="locations">BRISBANE &amp; MELBOURNE</p>
    <p class="headline-main">MOBILE</p>
    <p class="headline-sub">TYRE FITTING</p>
    <ul class="benefits">
      <li>easier</li>
      <li>faster</li>
      <li>cheaper</li>
    </ul>
    <p class="site-address">www.lowtreadhub.com.au</p>
  </section>

</main>
</body>
</html>
```